Velmora Datatech Solutions- Computer Network Company

Wordpress designs.

I want a web design that is up scale looking, high-end. A very modern and clean looking.

Thinking of rotating pictures of Network Management (picture of server/desktop computer), Backup Solutions (picture of server after fire), Network wiring (picture maybe of racks/switches, etc)

Service- Backup Solutions, Managing computers and servers, Database management, Network Wiring, Phone system management

Products we sell Tovo computers, KX printers,
About the company
Contact us

Target Market(s)

Companies looking for Computer support, Law office, Private business

Industry/Entity Type

Computer

Coding

Coded - Design and coding required

Font styles to use
Sans Serif

Requirements
Must have
• Wordpress design, will be hosted on a Linux server.
• Use the logo in the design, Clean, Up scale website
• Navigation- Services-Products -About Us-Contact Us
• ***Also, a link for Buying a domain (we are a reseller of hosting and domain names)*****
Nice to have
• picture rotation on the landing page, Network Management,

```html
<!DOCTYPE html>
<html lang="en">
<head>
<meta charset="utf-8">
<title>Velmora Datatech Solutions</title>
<link rel="stylesheet" href="https://fonts.googleapis.com/css2?family=Signika:wght@400;600&family=Open+Sans:wght@400;600;700&display=swap">
<style>
:root{
  --navy:#1d3f8c;
  --blue:#2f5fc4;
  --hero-blue:#3f6fd0;
  --green:#1e6b3c;
  --dark:#1f1f1f;
  --footer:#2b2b2b;
  --bottom:#151515;
  --ink:#111;
  --muted:#555;
  --light:#ececec;
  --white:#fff;
}
*{box-sizing:border-box;margin:0;padding:0}
html,body{width:1200px;height:2711px;overflow:hidden}
body{position:relative;font-family:"Open Sans",sans-serif;color:var(--ink);background:var(--white)}
.abs{position:absolute}
h1,h2,h3,.heading{font-family:"Signika",sans-serif;font-weight:400}

/* header */
.site-header{left:0;top:0;width:1200px;height:130px;background:var(--white);border-top:3px solid var(--green);box-shadow:0 2px 6px rgba(0,0,0,.08)}
.brand{left:60px;top:40px;display:flex;align-items:center;gap:12px}
.brand-dot{width:34px;height:34px;border-radius:50%;background:var(--navy)}
.brand-name{font-family:"Signika",sans-serif;font-weight:600;font-size:23px;color:var(--navy);line-height:1.1;width:220px}
.topbar-phone{left:867px;top:0;width:162px;height:40px;background:var(--green);color:var(--white);font-size:15px;display:flex;align-items:center;gap:12px;padding-left:14px;white-space:nowrap}
.topbar-social{left:1034px;top:6px;display:flex;gap:6px}
.social-dot{width:29px;height:29px;border-radius:50%;border:2px solid #222}
.main-nav{left:475px;top:69px;display:flex;align-items:center;gap:0}
.main-nav a{font-size:14.5px;font-weight:600;color:#111;text-decoration:none;text-transform:uppercase;padding:0 16px;line-height:36px;white-space:nowrap}
.main-nav a.active{background:var(--blue);color:var(--white);padding:0 18px}

/* hero */
.hero{left:0;top:130px;width:1200px;height:571px;background:radial-gradient(ellipse at 50% 40%,#d9f0fb 0%,#8fcbec 45%,#3b8fcc 100%)}
.hero-line{left:249px;top:365px;width:719px;height:70px;background:var(--hero-blue);color:var(--white);font-family:"Signika",sans-serif;font-weight:400;font-size:35px;letter-spacing:.5px;text-align:center;line-height:70px;text-transform:uppercase;white-space:nowrap;overflow:hidden}
.hero-line.second{left:262px;top:439px;width:692px;height:67px;background:var(--green);line-height:67px}
.hero-arrow{top:377px;width:34px;height:62px;background:var(--white);display:flex;align-items:center;justify-content:center}

/* welcome */
.welcome-title{left:0;top:770px;width:1200px;text-align:center;font-size:46px;color:#111;white-space:nowrap}
.welcome-title strong{font-weight:600;color:var(--navy)}
.welcome-text{left:120px;top:876px;width:960px;text-align:center;font-size:14.5px;line-height:26px;color:#333}
.partner{top:960px;height:97px;display:flex;align-items:center;justify-content:center;font-family:"Signika",sans-serif;font-weight:600;font-size:52px}
.partner.tovo{left:394px;width:193px;border:2px solid #333;color:var(--navy);background:var(--white)}
.partner.kx{left:616px;width:154px;background:var(--navy);color:var(--white);border:2px solid #10265a}

/* services */
.services{left:0;top:1126px;width:1200px;height:678px;background:radial-gradient(ellipse at 50% 40%,#3a2e2a 0%,#1a1716 70%,#111 100%)}
.services-title{left:0;top:1198px;width:1200px;text-align:center;color:var(--white);font-size:44px}
.service-hub{left:405px;top:1338px;width:350px;height:355px;border-radius:50%;background:var(--white)}
.hub-name{left:470px;top:1494px;width:220px;text-align:center;font-family:"Signika",sans-serif;font-weight:600;font-size:22px;color:var(--navy);line-height:1.15}
.service-icon{width:116px;height:116px;border-radius:50%;background:var(--blue);border:4px solid #fff;display:flex;align-items:center;justify-content:center}
.service-item{color:var(--white);width:290px}
.service-item h3{font-size:22px;font-weight:400;margin-bottom:10px;white-space:nowrap}
.service-item p{font-size:12.5px;line-height:19px}
.service-item.left{text-align:center}
.service-item.right{text-align:left}

/* reseller + support */
.reseller{left:0;top:1804px;width:620px;height:375px;background:var(--light)}
.reseller-title{left:64px;top:1852px;font-size:36px;color:#111;white-space:nowrap}
.reseller-title span{color:var(--blue)}
.reseller-rule{left:64px;top:1910px;width:260px;height:2px;background:#777}
.reseller-sub{left:62px;top:1924px;font-size:15.5px;font-weight:700}
.reseller-text{left:62px;top:1958px;width:510px;font-size:12.5px;line-height:21px;color:#555}
.btn-domain{left:60px;top:2069px;width:221px;height:47px;background:var(--green);color:var(--white);font-size:16px;display:flex;align-items:center;justify-content:center}
.support{left:620px;top:1804px;width:580px;height:375px;background:var(--navy)}
.support-title{left:681px;top:1858px;font-size:28px;color:var(--white);white-space:nowrap}
.support-text{left:681px;top:1896px;width:460px;font-size:14.5px;line-height:19px;color:var(--white)}
.field{left:681px;width:409px;height:40px;background:var(--white);border-radius:3px;font-size:13px;color:#999;padding:0 14px;display:flex;align-items:center}
.btn-submit{left:681px;top:2101px;width:166px;height:47px;background:var(--white);color:#111;border-radius:3px;font-size:16px;display:flex;align-items:center;justify-content:center}

/* call */
.call-title{left:0;top:2244px;width:1200px;text-align:center;font-size:29px;color:#111;white-space:nowrap}
.call-line{left:0;top:2296px;width:1200px;display:flex;justify-content:center;align-items:center;gap:14px;font-size:24px;font-weight:400;font-family:"Signika",sans-serif}

/* footer */
.site-footer{left:0;top:2378px;width:1200px;height:291px;background:var(--footer)}
.footer-brand{left:60px;top:2498px;display:flex;align-items:center;gap:14px}
.footer-brand .brand-dot{background:var(--white)}
.footer-brand .brand-name{color:var(--white);font-size:26px;width:260px}
.footer-head{top:2424px;font-size:22px;font-weight:400;color:var(--white);white-space:nowrap}
.footer-field{left:426px;width:218px;background:var(--white);border-radius:2px;font-size:12.5px;color:#888;padding:8px 10px}
.btn-send{left:555px;top:2584px;width:86px;height:38px;background:var(--blue);color:var(--white);font-size:16px;display:flex;align-items:center;justify-content:center;border-radius:2px}
.quick-links{left:714px;top:2468px;list-style:none}
.quick-links li{color:var(--white);font-size:12.5px;line-height:27px;padding-left:16px;position:relative}
.quick-links li::before{content:"";position:absolute;left:2px;top:11px;width:5px;height:5px;border-radius:50%;background:var(--blue)}
.contact-list{left:918px;top:2470px;list-style:none}
.contact-list li{color:var(--white);font-size:13px;line-height:33px;display:flex;align-items:center;gap:12px;white-space:nowrap}
.footer-social{left:922px;top:2575px;display:flex;gap:5px}
.footer-social .social-dot{border:0;background:#ddd;width:28px;height:28px}
.bottom-bar{left:0;top:2669px;width:1200px;height:42px;background:var(--bottom);color:var(--white);font-size:12px;text-align:center;line-height:42px}
</style>
</head>
<body>

<header class="site-header abs"></header>
<div class="brand abs"><span class="brand-dot"></span><span class="brand-name">Velmora Datatech Solutions</span></div>
<div class="topbar-phone abs">
  <svg width="16" height="16" viewBox="0 0 24 24"><path fill="#fff" d="M6.6 10.8a15 15 0 0 0 6.6 6.6l2.2-2.2a1 1 0 0 1 1-.25 11.4 11.4 0 0 0 3.6.57 1 1 0 0 1 1 1V20a1 1 0 0 1-1 1A17 17 0 0 1 3 4a1 1 0 0 1 1-1h3.5a1 1 0 0 1 1 1c0 1.25.2 2.45.57 3.57a1 1 0 0 1-.25 1z"/></svg>
  800-555-0147
</div>
<div class="topbar-social abs"><span class="social-dot"></span><span class="social-dot"></span><span class="social-dot"></span></div>
<nav class="main-nav abs">
  <a class="active" href="#">Home</a><a href="#">Services</a><a href="#">Products</a><a href="#">About Us</a><a href="#">Buy a Domain</a><a href="#">Contact Us</a>
</nav>

<section class="hero abs" role="img" aria-label="Rotating photo of networked laptops around a glowing globe"></section>
<div class="hero-line abs">A place of your complete solutions</div>
<div class="hero-line second abs">We fullfills all technology needs</div>
<div class="hero-arrow abs" style="left:0"><svg width="14" height="24" viewBox="0 0 14 24"><path d="M12 2 2 12l10 10" fill="none" stroke="#222" stroke-width="2.5"/></svg></div>
<div class="hero-arrow abs" style="left:1166px"><svg width="14" height="24" viewBox="0 0 14 24"><path d="M2 2l10 10L2 22" fill="none" stroke="#222" stroke-width="2.5"/></svg></div>

<h1 class="welcome-title abs">Welcome to <strong>Velmora</strong></h1>
<p class="welcome-text abs">Lorem Ipsum is simply dummy text of the printing and typesetting industry. Lorem Ipsum has been the industry's standard dummy text ever since the 1500s, when an unknown printer took a galley of type and scrambledit to make a type specimen book.</p>
<div class="partner tovo abs">Tovo</div>
<div class="partner kx abs">KX</div>

<section class="services abs" role="img" aria-label="Dark background photo with faint user and network icons"></section>
<h2 class="services-title abs">Services we provide</h2>
<div class="service-hub abs"></div>
<div class="hub-name abs">Velmora Datatech Solutions</div>

<svg class="abs" style="left:0;top:0" width="1200" height="2711" aria-hidden="true">
  <g stroke="#fff" stroke-width="2" fill="#fff">
    <line x1="298" y1="1389" x2="385" y2="1389"/><path d="M292 1389l8-5v10z"/>
    <line x1="270" y1="1517" x2="345" y2="1517"/><path d="M264 1517l8-5v10z"/>
    <line x1="316" y1="1661" x2="392" y2="1661"/><path d="M310 1661l8-5v10z"/>
    <line x1="770" y1="1389" x2="848" y2="1389"/><path d="M856 1389l-8-5v10z"/>
    <line x1="815" y1="1521" x2="880" y2="1521"/><path d="M888 1521l-8-5v10z"/>
    <line x1="750" y1="1661" x2="842" y2="1661"/><path d="M850 1661l-8-5v10z"/>
  </g>
</svg>

<div class="service-icon abs" style="left:388px;top:1337px"><svg width="54" height="40" viewBox="0 0 54 40"><path d="M14 36a12 12 0 0 1-1-24 15 15 0 0 1 28 2 11 11 0 0 1 1 22z" fill="#fff"/><path d="M27 32V18m-7 6 7-7 7 7" stroke="#2f5fc4" stroke-width="4" fill="none"/></svg></div>
<div class="service-icon abs" style="left:650px;top:1337px"><svg width="48" height="48" viewBox="0 0 48 48"><g fill="#fff"><circle cx="36" cy="10" r="7"/><circle cx="12" cy="24" r="7"/><circle cx="36" cy="38" r="7"/></g><path d="M36 10 12 24l24 14" stroke="#fff" stroke-width="4" fill="none"/></svg></div>
<div class="service-icon abs" style="left:349px;top:1463px"><svg width="52" height="46" viewBox="0 0 52 46"><rect x="3" y="3" width="46" height="30" rx="3" fill="none" stroke="#fff" stroke-width="4"/><path d="M18 43h16M26 33v10" stroke="#fff" stroke-width="4"/></svg></div>
<div class="service-icon abs" style="left:697px;top:1463px"><svg width="48" height="48" viewBox="0 0 24 24"><path fill="#fff" d="M6.6 10.8a15 15 0 0 0 6.6 6.6l2.2-2.2a1 1 0 0 1 1-.25 11.4 11.4 0 0 0 3.6.57 1 1 0 0 1 1 1V20a1 1 0 0 1-1 1A17 17 0 0 1 3 4a1 1 0 0 1 1-1h3.5a1 1 0 0 1 1 1c0 1.25.2 2.45.57 3.57a1 1 0 0 1-.25 1z"/></svg></div>
<div class="service-icon abs" style="left:396px;top:1594px"><svg width="50" height="50" viewBox="0 0 50 50"><g fill="#fff"><ellipse cx="20" cy="9" rx="16" ry="6"/><path d="M4 14c0 4 7 6 16 6s16-2 16-6v7c0 4-7 6-16 6S4 25 4 21zM4 27c0 4 7 6 16 6l2 0v8h-2C11 41 4 39 4 35z"/></g><circle cx="34" cy="34" r="8" fill="none" stroke="#fff" stroke-width="3.5"/><path d="M40 40l6 6" stroke="#fff" stroke-width="4"/></svg></div>
<div class="service-icon abs" style="left:630px;top:1594px"><svg width="46" height="46" viewBox="0 0 46 46"><g fill="#fff"><rect x="4" y="3" width="38" height="10" rx="1"/><rect x="4" y="16" width="38" height="10" rx="1"/><rect x="4" y="29" width="38" height="10" rx="1"/></g><g fill="#2f5fc4"><circle cx="10" cy="8" r="2"/><circle cx="10" cy="21" r="2"/><circle cx="10" cy="34" r="2"/></g><path d="M4 44h38" stroke="#fff" stroke-width="2"/></svg></div>

<div class="service-item left abs" style="left:20px;top:1375px"><h3>Backup Solutions</h3><p>She packed her seven versalia, put her<br>into the belt and made on the way.</p></div>
<div class="service-item left abs" style="left:0;top:1503px"><h3>Managing computers</h3><p>She packed her seven versalia, put<br>her into the belt and made on the<br>way. When she reached the first .</p></div>
<div class="service-item left abs" style="left:30px;top:1648px"><h3>Database management</h3><p>She packed her seven versalia, put her<br>into the belt and made on the way.</p></div>
<div class="service-item right abs" style="left:868px;top:1375px"><h3>Network Wiring</h3><p>She packed her seven versalia, put<br>her into the belt and made on the way.</p></div>
<div class="service-item right abs" style="left:895px;top:1503px"><h3>Phone system management</h3><p>She packed her seven versalia, put her<br>into the belt and made on the way.</p></div>
<div class="service-item right abs" style="left:860px;top:1646px"><h3>Servers</h3><p>She packed her seven versalia, put her into<br>the belt and made on the way. When she<br>reached the first .</p></div>

<section class="reseller abs"></section>
<h2 class="reseller-title abs">We are a reseller with <span>Domainly</span></h2>
<div class="reseller-rule abs"></div>
<p class="reseller-sub abs">Are you looking for a Domain with domainly?</p>
<p class="reseller-text abs">Lorem Ipsum is simply dummy text of the printing and typesetting industry. Lorem Ipsum has been the industry's standard dummy text ever since the 1500s, when an unknown printer took a galley of type and scrambled it to make a type specimen book. It has survived not only five centuries.</p>
<div class="btn-domain abs">Buying a Domain name</div>

<section class="support abs"></section>
<h2 class="support-title abs">Looking for Computer support?</h2>
<p class="support-text abs">Contact with us Today we solve your all issue and provide you solutions</p>
<div class="field abs" style="top:1957px">Name</div>
<div class="field abs" style="top:2002px">Email</div>
<div class="field abs" style="top:2047px">Phone no</div>
<div class="btn-submit abs">Submit Query</div>

<h2 class="call-title abs">Reach out to us for Business, Query, Buy or sell computers and Support</h2>
<div class="call-line abs">Call us Today
  <svg width="36" height="36" viewBox="0 0 36 36"><circle cx="18" cy="18" r="16" fill="none" stroke="#111" stroke-width="2"/><path transform="translate(8 8) scale(.85)" fill="#111" d="M6.6 10.8a15 15 0 0 0 6.6 6.6l2.2-2.2a1 1 0 0 1 1-.25 11.4 11.4 0 0 0 3.6.57 1 1 0 0 1 1 1V20a1 1 0 0 1-1 1A17 17 0 0 1 3 4a1 1 0 0 1 1-1h3.5a1 1 0 0 1 1 1c0 1.25.2 2.45.57 3.57a1 1 0 0 1-.25 1z"/></svg>
  (555) 014 732</div>

<footer class="site-footer abs"></footer>
<div class="footer-brand abs"><span class="brand-dot"></span><span class="brand-name">Velmora Datatech Solutions</span></div>
<h3 class="footer-head abs" style="left:424px">Query us</h3>
<div class="footer-field abs" style="top:2476px;height:36px">Email</div>
<div class="footer-field abs" style="top:2518px;height:56px">Your Message</div>
<div class="btn-send abs">Send</div>
<h3 class="footer-head abs" style="left:712px">Quick Links</h3>
<ul class="quick-links abs"><li>About Us</li><li>Privacy Policy</li><li>Terms &amp; Condition</li><li>Best Seller</li><li>Manufactures</li></ul>
<h3 class="footer-head abs" style="left:917px">Contact us</h3>
<ul class="contact-list abs">
  <li><svg width="18" height="18" viewBox="0 0 24 24"><path fill="#4d7fe0" d="M6.6 10.8a15 15 0 0 0 6.6 6.6l2.2-2.2a1 1 0 0 1 1-.25 11.4 11.4 0 0 0 3.6.57 1 1 0 0 1 1 1V20a1 1 0 0 1-1 1A17 17 0 0 1 3 4a1 1 0 0 1 1-1h3.5a1 1 0 0 1 1 1c0 1.25.2 2.45.57 3.57a1 1 0 0 1-.25 1z"/></svg>Phone: 800-555-0147</li>
  <li><svg width="18" height="18" viewBox="0 0 24 24"><g fill="none" stroke="#4d7fe0" stroke-width="2"><rect x="6" y="2" width="12" height="6"/><rect x="3" y="8" width="18" height="9" rx="1"/><rect x="6" y="14" width="12" height="7"/></g></svg>Fax: 555-013-9920</li>
  <li><svg width="18" height="14" viewBox="0 0 24 18"><rect x="1" y="1" width="22" height="16" fill="#4d7fe0"/><path d="M1 1l11 9 11-9" stroke="#2b2b2b" stroke-width="2" fill="none"/></svg>Email: hello@velmoradata.com</li>
</ul>
<div class="footer-social abs"><span class="social-dot"></span><span class="social-dot"></span><span class="social-dot"></span><span class="social-dot"></span><span class="social-dot"></span></div>
<div class="bottom-bar abs">©2016 VELMORA ALL RIGHT RESERVED</div>

</body>
</html>
```